LQM Values Puzzle Pieces

I want to use my logo (symbol only, not the words Marlowe Vein Center) as the basis of the puzzle and incorporate our four values into the logo as four puzzle pieces. I want each puzzle piece to have one value on it and a line extending from the piece. At this point, I would like the bullet points of each value to be listed.
Here are the four values with the bullet points:
Cheese Movers
Are open to and embrace change, recognizing that it is a process, not a one-time event.
Are lifelong learners who continually use incremental improvements to enhance their knowledge and skills.
Possess grit, a combination of passion and perseverance, which allows them to overcome challenges and achieve their goals. Grit is the fuel to stay motivated and determined even when faced with obstacles or setbacks.
Are self-disciplined, working smart in thought and action by intentionally focusing on their goals.
Servant-Minded
Approaches work with humility, grace, and mercy, recognizing that serving others is a privilege.
Have a patient-centric approach, looking at the processes through the patient's eyes to ensure the best possible experience.
Educating patients with clarity and consistency, ensuring that they understand vein disease is a treatable but not curable condition.
The "My Mother Rule" is a guiding principle that everyone is treated with respect, care, and compassion like our beloved family members.
We seek to provide vein care to all who need it.
Better Together
We emphasize the importance of having a team that rows in the same direction towards a common goal.
We have accountability and integrity by taking responsibility for our actions and their impact on others.
We are courageously real, speaking authentically to share thoughts and ideas while feeling valued for our unique perspectives.
We prioritize creating a supportive environment where team members feel they have the resources needed to succeed.
Balanced
We emphasize the importance of maintaining a work-life balance.
We are professional and take what we do seriously while still using laughter and fun to create a welcoming and friendly environment for patients and staff.
Valuable output is the greatest measure, not hours put in. Anyone can keep busy, but that does not equate to productivity.
Look and feel
Each slider illustrates characteristics of the customer's brand and the style your logo design should communicate.

```html
<!DOCTYPE html>
<html lang="en">
<head>
<meta charset="utf-8">
<title>LQM Values</title>
<link href="https://fonts.googleapis.com/css2?family=Roboto:wght@400;700&display=swap" rel="stylesheet">
<style>
  :root {
    --navy: #2a347a;
    --green: #0d8543;
    --slate: #778895;
    --white: #ffffff;
  }
  html, body {
    margin: 0;
    padding: 0;
    overflow: hidden;
    background: var(--white);
  }
  .canvas {
    position: relative;
    width: 1200px;
    height: 1200px;
    overflow: hidden;
    background: var(--white);
    font-family: "Roboto", Arial, sans-serif;
    color: var(--white);
  }
  .quadrant {
    position: absolute;
  }
  .quadrant--change   { left: 65px;  top: 64px;  width: 519px; height: 520px; background: var(--navy); }
  .quadrant--service  { left: 617px; top: 64px;  width: 519px; height: 520px; background: var(--navy); }
  .quadrant--team     { left: 65px;  top: 616px; width: 522px; height: 520px; background: var(--green); }
  .quadrant--balance  { left: 619px; top: 616px; width: 517px; height: 520px; background: var(--slate); }

  .value {
    position: absolute;
  }
  .value--change  { left: 107px; top: 112px; }
  .value--service { left: 656px; top: 112px; }
  .value--team    { left: 107px; top: 669px; }
  .value--balance { left: 771px; top: 682px; }

  .value__title {
    margin: 0 0 1px;
    font-size: 21px;
    font-weight: 700;
    line-height: 26px;
  }
  .value__list {
    list-style: none;
    margin: 0;
    padding: 0;
    font-size: 18px;
    line-height: 24px;
    font-weight: 400;
  }
  .value__list li {
    position: relative;
    padding-left: 12px;
  }
  .value__list li::before {
    content: "";
    position: absolute;
    left: 0;
    top: 9px;
    width: 7px;
    height: 7px;
    border-radius: 50%;
    background: var(--white);
  }

  .hub {
    position: absolute;
    left: 438px;
    top: 441px;
    width: 326px;
    height: 326px;
    border-radius: 50%;
    background: var(--white);
    display: flex;
    align-items: center;
    justify-content: center;
  }
  .hub__name {
    font-size: 60px;
    font-weight: 700;
    color: var(--navy);
    letter-spacing: 2px;
  }
</style>
</head>
<body>
<div class="canvas">
  <div class="quadrant quadrant--change"></div>
  <div class="quadrant quadrant--service"></div>
  <div class="quadrant quadrant--team"></div>
  <div class="quadrant quadrant--balance"></div>

  <section class="value value--change">
    <h2 class="value__title">Cheese Movers</h2>
    <ul class="value__list">
      <li>Are open to and embrace change,<br>recognizing that it is a process, not a<br>one-time event.</li>
      <li>Are lifelong learners who continually use<br>incremental improvements to<br>enhance their knowledge and skills.</li>
      <li>Possess grit, a combination of<br>passion and perseverance, which allows<br>them to overcome challenges and<br>achieve their goals.Grit is the fuel to stay<br>motivated and determined even when<br>faced with obstacles or setbacks.</li>
      <li>Are self-disciplined, working smart in<br>thought and action by intentionally<br>focusing on their goals</li>
    </ul>
  </section>

  <section class="value value--service">
    <h2 class="value__title">Servant-Minded</h2>
    <ul class="value__list">
      <li>Approaches work with humility, grace, and<br>mercy, recognizing that serving others is a<br>privilege.</li>
      <li>Have a patient-centric approach, looking at<br>the processes through the patient's eyes to<br>ensure the best possible experience.</li>
      <li>Educating patients with clarity and consistency,<br>ensuring that they understand vein disease is a<br>treatable but not curable condition.</li>
      <li>The "My Mother Rule" is a guiding principle that<br>everyone is treated with respect, care, and<br>compassion like our beloved family members.</li>
      <li>We seek to provide vein care to all who need it.</li>
    </ul>
  </section>

  <section class="value value--team">
    <h2 class="value__title">Better Together</h2>
    <ul class="value__list">
      <li>We emphasize the importance of having<br>a team that rows in the same direction<br>towards a common goal.</li>
      <li>We have accountability and integrity by<br>taking responsibility for our<br>actions and their impact on others.</li>
      <li>We are courageously real, speaking au-<br>thentically to share thoughts and ideas<br>while feeling valued for our unique per-<br>spectives.</li>
      <li>We prioritize creating a supportive envi-<br>ronment where team members feel they<br>have the resources needed to succeed.</li>
    </ul>
  </section>

  <section class="value value--balance">
    <h2 class="value__title">Balanced</h2>
    <ul class="value__list">
      <li>We emphasize the importance of<br>maintaining a work-life balance.</li>
      <li>We are professional and take what<br>we do seriously while still using<br>laughter and fun to create a<br>welcoming and friendly enviroment<br>for patients and staff.</li>
      <li>Valuable output is the greatest<br>measure, not hours put in. Anyone<br>can keep busy, but that does not<br>equate to productivity.</li>
    </ul>
  </section>

  <div class="hub">
    <span class="hub__name">LQM</span>
  </div>
</div>
</body>
</html>
```